Flyer "Pinch Analysis"-Energy Optimization procedure for Industry

We need a flyer (1xA4 recto/verso )design for a new part of our business.

In Summary: we want to communicate that we are providing "Pinch Analysis" for the industry. It's an energy optimization procedure. We are a cutting edge engineering consulting group.

All details about project in the attached files

Target Market(s)

Engineering

Industry/Entity Type

Business

Font styles to use
Serif

Requirements
Must have
• Finale document in .ai format ready for printing
• More informations in attached files
Nice to have
• See attached files

```html
<!DOCTYPE html>
<html lang="fr">
<head>
<meta charset="utf-8">
<title>Analyse Pinch – Thermova</title>
<link href="https://fonts.googleapis.com/css2?family=Michroma&family=Raleway:ital,wght@0,400;0,500;0,700;1,700&display=swap" rel="stylesheet">
<style>
:root{
  --blue:#2ab4e8;
  --blue-deep:#1e3a5c;
  --red:#e2262a;
  --ink:#2a2a2a;
  --grey:#555b62;
  --white:#ffffff;
  --panel:#f4f8fb;
  --frame:#36b6e6;
}
*{box-sizing:border-box;margin:0;padding:0}
html,body{width:850px;height:1200px;overflow:hidden;background:var(--white)}
body{position:relative;font-family:"Raleway",Arial,sans-serif;color:var(--ink)}
.hero-photo{position:absolute;left:0;top:0;width:850px;height:606px;
  background:linear-gradient(180deg,#3e4a56 0%,#6b7784 30%,#a9b4bf 70%,#7c8995 100%)}
.hero-band{position:absolute;left:0;top:168px;width:850px;height:282px;background:rgba(28,36,46,.72)}
.brand{font-family:"Michroma",Arial,sans-serif;color:var(--blue);white-space:nowrap;line-height:1}
.brand-top{position:absolute;right:26px;top:76px;font-size:26px;letter-spacing:1px}
.hero-title{position:absolute;left:30px;top:204px;font-family:"Michroma",Arial,sans-serif;color:var(--white);font-size:31px;line-height:40px;letter-spacing:1px;font-weight:400}
.hero-sub{position:absolute;left:30px;top:254px;border-left:4px solid var(--red);padding-left:24px;font-size:22px;line-height:28px;color:var(--blue)}
.hero-sub b{font-weight:700}
.chart{position:absolute;left:450px;top:170px}
.content{position:absolute;left:0;top:606px;width:850px;height:594px;border:5px solid var(--frame);border-top:none;background:var(--white)}
.panel{position:absolute;left:505px;top:6px;width:330px;height:578px;background:var(--panel)}
.section-title{position:absolute;left:38px;top:40px;font-family:"Michroma",Arial,sans-serif;color:var(--red);font-size:16px;line-height:20px;font-weight:400;white-space:nowrap}
.section-sub{position:absolute;left:38px;top:63px;font-size:11.5px;line-height:14px;font-weight:700;letter-spacing:1px;color:var(--grey);text-transform:uppercase;white-space:nowrap}
.col{position:absolute;top:102px;width:218px;font-size:10.8px;line-height:16.5px;text-align:justify;color:var(--ink);hyphens:auto;-webkit-hyphens:auto}
.col p{margin-bottom:16px}
.col-a{left:36px}
.col-b{left:274px;width:222px}
.col ul{list-style:none}
.col li{position:relative;padding-left:16px;margin-bottom:4px;text-align:left}
.col li::before{content:"";position:absolute;left:2px;top:4px;border-left:5px solid var(--red);border-top:4px solid transparent;border-bottom:4px solid transparent}
.col strong{font-weight:700}
.brand-panel{position:absolute;left:540px;top:70px;font-size:24px;letter-spacing:1px}
.panel-title{position:absolute;left:532px;top:208px;font-family:"Michroma",Arial,sans-serif;color:var(--blue-deep);font-size:22px;line-height:28px;font-weight:400;white-space:nowrap}
.panel-sub{position:absolute;left:550px;top:244px;font-size:17px;line-height:24px;color:var(--grey)}
.panel-sub b{font-weight:700}
.contact{position:absolute;right:40px;top:436px;text-align:right}
.contact-label{font-family:"Michroma",Arial,sans-serif;color:var(--red);font-size:12px;display:flex;align-items:center;justify-content:flex-end;gap:5px}
.contact-names{margin-top:8px;font-size:11.5px;font-weight:700;font-style:italic;color:var(--ink)}
.brand-small{margin-top:12px;font-size:14px;color:var(--grey)}
.address{margin-top:10px;font-size:11.5px;font-style:italic;line-height:17px;color:var(--ink)}
</style>
</head>
<body>
<div class="hero-photo" role="img" aria-label="Photographie d'une installation industrielle avec tuyauteries métalliques"></div>
<div class="hero-band"></div>
<div class="brand brand-top">THERMOVA</div>
<h1 class="hero-title">ANALYSE PINCH</h1>
<p class="hero-sub">En route vers la<br><b>performance énergétique</b></p>

<svg class="chart" width="400" height="270" viewBox="450 170 400 270" aria-label="Courbes composites chaude et froide">
  <rect x="702" y="172" width="148" height="15" fill="var(--blue)"/>
  <text x="712" y="183" font-family="Raleway" font-size="9" fill="#fff">Hot and Cold composite curves</text>
  <g stroke="rgba(255,255,255,.35)" stroke-width="1">
    <line x1="510" y1="210" x2="824" y2="210"/><line x1="510" y1="233" x2="824" y2="233"/>
    <line x1="510" y1="256" x2="824" y2="256"/><line x1="510" y1="278" x2="824" y2="278"/>
    <line x1="510" y1="301" x2="824" y2="301"/><line x1="510" y1="324" x2="824" y2="324"/>
    <line x1="510" y1="347" x2="824" y2="347"/><line x1="510" y1="369" x2="824" y2="369"/>
    <line x1="549" y1="210" x2="549" y2="392"/><line x1="589" y1="210" x2="589" y2="392"/>
    <line x1="628" y1="210" x2="628" y2="392"/><line x1="667" y1="210" x2="667" y2="392"/>
    <line x1="706" y1="210" x2="706" y2="392"/><line x1="745" y1="210" x2="745" y2="392"/>
    <line x1="785" y1="210" x2="785" y2="392"/><line x1="824" y1="210" x2="824" y2="392"/>
  </g>
  <line x1="510" y1="205" x2="510" y2="392" stroke="#fff" stroke-width="1.5"/>
  <line x1="510" y1="392" x2="826" y2="392" stroke="#fff" stroke-width="1.5"/>
  <g font-family="Raleway" font-size="8" fill="#fff" text-anchor="end">
    <text x="503" y="213">160</text><text x="503" y="236">140</text><text x="503" y="259">120</text>
    <text x="503" y="281">100</text><text x="503" y="304">80</text><text x="503" y="327">60</text>
    <text x="503" y="350">40</text><text x="503" y="372">20</text><text x="503" y="395">0</text>
  </g>
  <g font-family="Raleway" font-size="8" fill="#fff" text-anchor="middle">
    <text x="510" y="406">0</text><text x="549" y="406">100</text><text x="589" y="406">200</text>
    <text x="628" y="406">300</text><text x="667" y="406">400</text><text x="706" y="406">500</text>
    <text x="745" y="406">600</text><text x="785" y="406">700</text><text x="824" y="406">800</text>
  </g>
  <rect x="456" y="314" width="14" height="100" fill="var(--blue)"/>
  <text transform="translate(466 412) rotate(-90)" font-family="Raleway" font-size="8" fill="#fff">Actual temperature (°C)</text>
  <rect x="472" y="419" width="78" height="15" fill="var(--blue)"/>
  <text x="477" y="430" font-family="Raleway" font-size="9" fill="#fff">Heat flow (kW)</text>
  <rect x="662" y="405" width="44" height="9" fill="rgba(255,255,255,.25)"/>
  <text x="665" y="412" font-family="Raleway" font-size="6" fill="#fff">Pinch ΔT</text>
  <polyline points="510,375 549,369 565,358 620,324 620,312" fill="none" stroke="var(--red)" stroke-width="2.5"/>
  <polyline points="541,386 573,369 667,324 683,233 793,233" fill="none" stroke="var(--blue)" stroke-width="2.5"/>
</svg>

<section class="content">
  <div class="panel"></div>
  <h2 class="section-title">ANALYSE PINCH</h2>
  <p class="section-sub">Performance opérationnelle et efficacité énergétique</p>
  <div class="col col-a">
    <p>La performance opérationnelle et l'efficacité énergétique sont les clés de la réussite de l'industrie de demain.</p>
    <p>Fort d'une longue expérience dans l'analyse, la conception et la mise en service d'installations industrielles (chimie, alimentaire, pharmacie,...), la société Thermova utilise l'analyse Pinch dans sa démarche de conception et d'amélioration.</p>
    <p>L'analyse Pinch est une méthode d'analyse systématique développée et appliquée depuis les années 1980; elle permet de répondre aux questions suivantes:</p>
    <ul>
      <li>Quels sont les besoins de chaleur et de froid minimaux de mon procédé</li>
      <li>Quel est mon potentiel de réduction de consommation énergétique</li>
      <li>Quel est la solution technique présentant les coûts minimaux entre investissements et économies</li>
    </ul>
  </div>
  <div class="col col-b">
    <p>L'amélioration de l'efficacité énergétique est liée directement à l'exploitation des potentiels de récupération du procédé. Des potentiels de diminution de la consommation de 10 à 30% sont usuels. Nous pouvons également améliorer les performances opérationnelles en analysant vos méthodes de fabrication.</p>
    <p>L'analyse Pinch est aussi bien adaptée pour les PME que pour les grandes entreprises dont les procédés sont exploités de manière continue ou discontinue (batch).</p>
    <p>Etant donné les objectifs énergétiques de la confédération, <strong>l'agence nationale de l'énergie (ANE) soutient les analyses Pinch à hauteur de 35% pour les procédés continus et de 60% pour les procédés discontinus (batch).</strong></p>
    <p>Pour tous compléments d'informations et pour savoir si une analyse Pinch est justifiée dans votre cas, nous vous conseillons avec plaisir.</p>
  </div>
  <div class="brand brand-panel">THERMOVA</div>
  <h2 class="panel-title">ANALYSE PINCH</h2>
  <p class="panel-sub">En route vers la<br><b>performance énergétique</b></p>
  <div class="contact">
    <div class="contact-label">CONTACT
      <svg width="9" height="12" viewBox="0 0 9 12"><path d="M4.5 0.8a3.7 3.7 0 0 0-3.7 3.7c0 2.8 3.7 6.8 3.7 6.8s3.7-4 3.7-6.8A3.7 3.7 0 0 0 4.5 0.8z" fill="none" stroke="var(--red)" stroke-width="1.4"/><circle cx="4.5" cy="4.5" r="1.3" fill="var(--red)"/></svg>
    </div>
    <p class="contact-names">Julien Marchand, Claire Deveaux</p>
    <div class="brand brand-small">THERMOVA</div>
    <p class="address">Thermova SA<br>Avenue des Forges 14<br>CH-1950 Sion</p>
  </div>
</section>
</body>
</html>
```